Tri-fold Brochure for Law Firm

Double-sided brochure to be folded into 6 sides tri-fold brochure for an estate planning special for new parents or parents-to-be. Brochure will be placed in classes for new parents/young parents.

Target Market(s)

New Parents Aged 24-34

Industry/Entity Type

Law Firm

Font styles to use
Serif

Requirements
Must have
• The information provided in the word document.
Nice to have
• Highlight the phrase "for New Parents."
• You may use the color scheme from our website:
• http://k47.9dw.sitevaultexample.com/

```html
<!DOCTYPE html>
<html lang="en">
<head>
<meta charset="utf-8">
<title>Estate Planning for New Parents – Tri-fold Brochure</title>
<link href="https://fonts.googleapis.com/css2?family=Montserrat:wght@700;800&family=Lato:wght@400;700&display=swap" rel="stylesheet">
<style>
  :root {
    --backdrop: #8a8a8a;
    --paper: #f4f4f6;
    --ink: #222226;
    --ink-soft: #3a3a40;
    --gold: #e0a92e;
    --gold-deep: #c98f17;
    --gold-bright: #f2c13a;
    --white: #ffffff;
    --callout-bg: #1e1a14;
    --rule: #2a2a2a;
  }
  * { box-sizing: border-box; margin: 0; padding: 0; }
  html, body { width: 1200px; height: 923px; overflow: hidden; }
  body { background: var(--backdrop); font-family: "Lato", "Helvetica Neue", Arial, sans-serif; color: var(--ink); }

  .brochure {
    position: absolute; left: 67px; top: 50px;
    width: 1066px; height: 823px;
    display: flex; background: var(--paper);
    box-shadow: 0 10px 30px rgba(0,0,0,.3);
  }
  .panel { position: relative; width: 355px; height: 100%; }
  .panel + .panel { border-left: 1px solid #dcdce0; }
  .panel--inside { width: 356px; }

  .hero {
    position: absolute; left: 0; top: 0; width: 710px; height: 262px; z-index: 2;
    background: linear-gradient(100deg, #3b2433 0%, #6b3f2a 28%, #b8772c 52%, #8a5a2a 72%, #4a3424 100%);
  }
  .hero__title {
    position: absolute; left: 56px; top: 140px;
    font-family: "Montserrat", Arial, sans-serif; font-weight: 800;
    color: var(--white); font-size: 24px; line-height: 1.45; letter-spacing: .3px;
    text-shadow: 0 1px 3px rgba(0,0,0,.4);
  }
  .hero__price { color: var(--gold-bright); font-size: 28px; }

  .panel__body { position: absolute; left: 0; right: 0; top: 262px; padding: 0 30px 0 36px; }
  .panel--inside .panel__body { padding: 0 28px 0 36px; }

  .section-title {
    font-family: "Montserrat", Arial, sans-serif; font-weight: 700;
    font-size: 16px; line-height: 1.2; color: var(--ink); margin-top: 30px;
  }
  .section-rule { position: relative; height: 2px; width: 255px; background: var(--rule); margin: 10px 0 14px; }
  .section-rule::before { content: ""; position: absolute; left: 0; top: -1px; width: 54px; height: 4px; background: var(--gold); }

  .copy { font-size: 13.4px; line-height: 1.45; color: var(--ink-soft); margin-bottom: 12px; }

  .callout {
    position: relative; margin: 8px -28px 0 -4px; padding: 22px 16px 12px 16px;
    background: var(--callout-bg); color: var(--gold-bright);
    font-size: 14px; line-height: 1.05;
  }
  .callout::before {
    content: ""; position: absolute; left: 12px; top: 0;
    border-left: 12px solid transparent; border-right: 12px solid transparent;
    border-top: 16px solid var(--gold);
  }

  .panel--cover { background: var(--gold); color: var(--white); padding: 56px 34px 0 34px; }
  .panel--cover .section-title { margin-top: 0; color: var(--ink); }
  .panel--cover .copy { color: #fff6e0; margin-top: 14px; font-size: 13.2px; }
  .panel--cover .section-title + .copy { margin-bottom: 20px; }

  .cover-photo {
    position: absolute; left: 0; right: 0; bottom: 0; height: 240px;
    background: linear-gradient(160deg, rgba(224,169,46,0) 0%, rgba(240,200,120,.35) 50%, rgba(201,143,23,.5) 100%);
  }
  .cover-cta { position: absolute; left: 50px; right: 30px; top: 610px; }
  .cover-cta__lead {
    font-family: "Montserrat", Arial, sans-serif; font-weight: 700;
    font-size: 17px; line-height: 1.3; color: var(--ink);
  }
  .cover-cta__call {
    margin-top: 22px; text-align: right;
    font-family: "Montserrat", Arial, sans-serif; font-weight: 800;
    font-size: 28px; line-height: 1.1; color: var(--ink);
  }
  .cover-cta__phone { display: block; color: var(--white); font-size: 28px; }
</style>
</head>
<body>
<main class="brochure">
  <div class="hero" role="img" aria-label="Photo of a wooden judge's gavel beside stacks of gold coins and law books">
    <h1 class="hero__title">FOR NEW PARENTS<br><span class="hero__price">$750</span> PER COUPLE</h1>
  </div>

  <section class="panel panel--inside">
    <div class="panel__body">
      <h2 class="section-title">Why should every parent<br>have a will?</h2>
      <div class="section-rule"></div>
      <p class="copy">Imagine how many people love your children. Would there be a fight over who would care for your children if you passed away without leaving instructions?</p>
      <p class="copy">Naming a guardian in your will helps avoid litigation that would cause additional stress to your children and loved ones. You can also name a back-up in the event that your first choice is unable or unwilling to serve as guardian.</p>
      <h2 class="section-title" style="margin-top:20px">What happens if I die in<br>Maryland without a will?</h2>
      <div class="section-rule"></div>
      <p class="copy">If you are married and have minor children, your spouse will inherit one half of your intestate property and your children will inherit the rest. If you have children but no spouse, your children will inherit everything.</p>
      <p class="copy">For most parents, this plan doesn't make sense.</p>
    </div>
  </section>

  <section class="panel panel--inside">
    <div class="panel__body" style="padding-top:30px">
      <p class="copy">Married people generally want their spouse to inherit all of their estate and unmarried people should have more control over how funds are distributed to their minor children.</p>
      <p class="copy">Furthermore, Maryland law doesn't take into account nontraditional families. For example, foster children and stepchildren that are not legally adopted will not automatically inherit a share of your estate.</p>
      <p class="callout">You can find the complete laws of intestacy (dying without a will) in the Maryland Code of Estates &amp; Trusts §§ 3-101 to 3-303.</p>
      <h2 class="section-title" style="margin-top:24px">Should we prepare a will now if we plan to have more children in the future?</h2>
      <div class="section-rule"></div>
      <p class="copy">There is no reason to put off drafting a will. A will can be written to treat your children as a "class" that would include any future children born to or adopted by you.</p>
    </div>
  </section>

  <section class="panel panel--cover">
    <div class="cover-photo" role="img" aria-label="Faint photo of a last will document with a pen"></div>
    <h2 class="section-title">What does the estate planning package include?</h2>
    <p class="copy">Our estate planning package includes a will, an advance medical directive, and a power of attorney. A will names a guardian for your children and gives instructions on how to distribute your probate property at death. An advance medical directive, also known as a living will, states directions regarding your healthcare decisions in the event that you can't make those decisions yourself. A power of attorney gives someone the ability to handle your financial affairs during your lifetime.</p>
    <h2 class="section-title">How long will the process take?</h2>
    <p class="copy">Before our first meeting, you will receive information to help you start thinking about some of the decisions we'll make during the initial consultation which lasts approximately one hour. It takes about 2 to 3 weeks after our initial meeting to draft your documents. You will receive draft copies of your documents to review before coming in for your last appointment to sign the documents in front of witnesses and a notary.</p>
    <div class="cover-cta">
      <p class="cover-cta__lead">For parents-to-be and parents of children under 5 years old.</p>
      <p class="cover-cta__call">Call Now<span class="cover-cta__phone">(410)-555-0148</span></p>
    </div>
  </section>
</main>
</body>
</html>
```